Flyer for Pharmacy/Medical Convention

Tri-fold flyer for pharmacy/medical convention. The inside of the flyer we would like to look like a venn diagram, possibly using an image similar to our blue logo

Copy write will be submitted when a design is chosen

there will be a flap about educational features, one about supplements an automated recommendations, and a flap about a computer platform to manage patients

Target Market(s)

Pharmacists and Medical Providers

Industry/Entity Type

Supplement

Colors

Designer to choose colors to be used in the design.

Requirements
Must have
• color scheme similar to logos and or label design attached

```html
<!DOCTYPE html>
<html lang="en">
<head>
<meta charset="utf-8">
<title>Solvane Health – Tri-fold Flyer</title>
<link rel="stylesheet" href="https://fonts.googleapis.com/css2?family=Fira+Sans+Condensed:ital,wght@0,400;0,500;1,400&display=swap">
<style>
  :root {
    --canvas-bg: #cbcbcb;
    --blue-light: #4a80bd;
    --blue-mid: #3b59a6;
    --blue-deep: #2a2a82;
    --sky: #5b8fd0;
    --band-top: #3745a8;
    --red: #e2232b;
    --white: #ffffff;
    --navy-text: #1c2a80;
    --grey-text: #666a72;
  }
  * { margin: 0; padding: 0; box-sizing: border-box; }
  html, body {
    width: 1200px; height: 1200px; overflow: hidden;
    background: var(--canvas-bg);
  }
  .canvas { position: relative; width: 1200px; height: 1200px; }
  .spread { position: absolute; display: block; }
  .spread--inside { left: 263px; top: 54px; width: 675px; height: 485px; }
  .spread--outside { left: 261px; top: 626px; width: 677px; height: 485px; }
  .body-copy {
    font-family: "Fira Sans Condensed", "Arial Narrow", sans-serif;
    font-size: 19px; fill: var(--white); text-anchor: middle;
  }
  .intro-copy {
    font-family: "Fira Sans Condensed", "Arial Narrow", sans-serif;
    font-style: italic; font-size: 17px; fill: var(--white);
  }
  .headline {
    font-family: "Fira Sans Condensed", "Arial Narrow", sans-serif;
    font-weight: 400; font-size: 26px; fill: var(--white); text-anchor: middle;
  }
  .image-hint {
    font-family: "Fira Sans Condensed", "Arial Narrow", sans-serif;
    font-style: italic; font-size: 19px; fill: var(--grey-text); text-anchor: middle;
  }
  .brand-name {
    font-family: "Fira Sans Condensed", "Arial Narrow", sans-serif;
    font-weight: 500; fill: var(--navy-text);
  }
  .fold { stroke: rgba(0,0,0,0.08); stroke-width: 2; }
</style>
</head>
<body>
<main class="canvas">

  <!-- Inside spread -->
  <svg class="spread spread--inside" viewBox="0 0 844 606" aria-label="Inside spread">
    <defs>
      <linearGradient id="inBlue" x1="0" y1="0" x2="0" y2="1">
        <stop offset="0" stop-color="var(--blue-light)"/>
        <stop offset="0.55" stop-color="var(--blue-mid)"/>
        <stop offset="1" stop-color="var(--blue-deep)"/>
      </linearGradient>
      <clipPath id="inClip"><rect width="844" height="606"/></clipPath>
    </defs>
    <g clip-path="url(#inClip)">
      <rect class="panel-bg" width="844" height="606" fill="url(#inBlue)"/>

      <!-- cover-side white circle -->
      <circle class="brand-circle" cx="-10" cy="-60" r="270" fill="var(--white)" stroke="var(--red)" stroke-width="6"/>

      <!-- image circle -->
      <circle class="image-circle" cx="790" cy="228" r="205" fill="var(--white)" stroke="var(--red)" stroke-width="6" role="img" aria-label="Image area for product photograph"/>

      <line class="fold" x1="279" y1="0" x2="279" y2="606"/>
      <line class="fold" x1="561" y1="0" x2="561" y2="606"/>
    </g>

    <g class="brand">
      <circle cx="54" cy="70" r="7" fill="var(--red)"/>
      <text class="brand-name" x="68" y="77" font-size="20">Solvane Health</text>
    </g>

    <text class="image-hint" x="741" y="188">add your</text>
    <text class="image-hint" x="745" y="213">image</text>

    <text class="body-copy" x="131" y="433">Lorem ipsum dolor sit amet,</text>
    <text class="body-copy" x="131" y="458">consectetuer adipiscing elit,</text>
    <text class="body-copy" x="131" y="483">sed diam nonummy nibh euis</text>
    <text class="body-copy" x="131" y="509">Lorem ipsum dolor sit amet,</text>
    <text class="body-copy" x="131" y="534">consectetuer adipiscing elit,</text>
    <text class="body-copy" x="131" y="559">sed diam nonummy nibh euis</text>

    <text class="body-copy" x="425" y="433">Lorem ipsum dolor sit amet,</text>
    <text class="body-copy" x="425" y="458">consectetuer adipiscing elit,</text>
    <text class="body-copy" x="425" y="483">sed diam nonummy nibh euis</text>
    <text class="body-copy" x="425" y="509">Lorem ipsum dolor sit amet,</text>
    <text class="body-copy" x="425" y="534">consectetuer adipiscing elit,</text>
    <text class="body-copy" x="425" y="559">sed diam nonummy nibh euis</text>

    <text class="intro-copy" x="604" y="491">Lorem ipsum dolor sit amet,</text>
    <text class="intro-copy" x="604" y="514">consectetuer adipiscing elit,</text>
    <text class="intro-copy" x="604" y="536">sed diam nonummy nibh euis</text>
  </svg>

  <!-- Outside spread -->
  <svg class="spread spread--outside" viewBox="0 0 847 606" aria-label="Outside spread">
    <defs>
      <linearGradient id="outBlue" x1="0" y1="0" x2="0" y2="1">
        <stop offset="0" stop-color="var(--blue-light)"/>
        <stop offset="0.5" stop-color="var(--blue-mid)"/>
        <stop offset="1" stop-color="var(--blue-deep)"/>
      </linearGradient>
      <linearGradient id="outSky" x1="0" y1="0" x2="0" y2="1">
        <stop offset="0" stop-color="var(--band-top)"/>
        <stop offset="1" stop-color="var(--sky)"/>
      </linearGradient>
      <clipPath id="outClip"><rect width="847" height="606"/></clipPath>
    </defs>
    <g clip-path="url(#outClip)">
      <rect class="panel-bg" width="847" height="606" fill="url(#outBlue)"/>
      <rect class="top-band" x="280" y="0" width="567" height="240" fill="url(#outSky)" role="img" aria-label="Decorative textured band"/>

      <!-- cover circle -->
      <circle class="brand-circle" cx="130" cy="106" r="208" fill="var(--white)" stroke="var(--red)" stroke-width="6"/>

      <!-- back image circle -->
      <circle class="image-circle" cx="735" cy="545" r="222" fill="var(--white)" role="img" aria-label="Image area for product photograph"/>

      <line class="fold" x1="282" y1="0" x2="282" y2="606"/>
      <line class="fold" x1="564" y1="0" x2="564" y2="606"/>
    </g>

    <g class="brand">
      <circle cx="48" cy="138" r="10" fill="var(--red)"/>
      <text class="brand-name" x="66" y="147" font-size="30">Solvane Health</text>
    </g>

    <text class="body-copy" x="137" y="399">Lorem ipsum dolor sit amet,</text>
    <text class="body-copy" x="137" y="424">consectetuer adipiscing elit,</text>
    <text class="body-copy" x="137" y="449">sed diam nonummy nibh euis</text>
    <text class="body-copy" x="137" y="475">Lorem ipsum dolor sit amet,</text>
    <text class="body-copy" x="137" y="500">consectetuer adipiscing elit,</text>
    <text class="body-copy" x="137" y="525">sed diam nonummy nibh euis</text>

    <text class="intro-copy" x="318" y="346">Lorem ipsum dolor sit amet,</text>
    <text class="intro-copy" x="318" y="369">consectetuer adipiscing elit,</text>
    <text class="intro-copy" x="318" y="391">sed diam nonummy nibh euis</text>

    <text class="headline" x="397" y="477">LOREM</text>
    <text class="headline" x="397" y="509">IPSUM DOLOR</text>

    <text class="image-hint" x="714" y="472">add your</text>
    <text class="image-hint" x="718" y="497">image</text>
  </svg>

</main>
</body>
</html>
```